New Menu for Elegant Cafe Pastry Shop

We need to choose a design and layout for our new menu. We would like to also condense our current menu to 4-6 pages.
We will be changing prices and items on the menu, so it needs to be editable. Adobe formats are preferred. The size of the pages needs to be letter size. We will be printing it in house
Please take inspiration from the photos of our shop and food and also our Instagram page.
Attached are our current menu our logo and the logo info

https://www.snapgrid.example/brioweldon/?hl=en
https://maps.example-locate.net/qT7mWx2KpLr9vBn4C

Industry/Entity Type

Food Cafe Bakery pastry

Font styles to use
Other font styles liked:
• please look at attached files

Colors

Designer to choose colors to be used in the design.

Requirements
Nice to have
• Use of Arches like on our shop wallpaper or oblong eclair shapes, Art Deco elements

```html
<!DOCTYPE html>
<html lang="en">
<head>
<meta charset="utf-8">
<title>brioweldon — Menu</title>
<link rel="stylesheet" href="https://fonts.googleapis.com/css2?family=Playfair+Display:wght@900&family=Open+Sans:wght@400;600;700&display=swap">
<style>
  :root{
    --rose:#b8625e;
    --rose-soft:#e9c9c4;
    --rose-faint:#f4e6e2;
    --paper:#fcf8f6;
    --ink:#2e2424;
    --muted:#5c4a48;
    --backdrop:#ece6e3;
  }
  *{box-sizing:border-box;margin:0;padding:0}
  html,body{width:1200px;height:960px;overflow:hidden;background:var(--backdrop);font-family:"Open Sans",sans-serif;color:var(--ink)}
  .spread{position:relative;width:1200px;height:960px}
  .page{position:absolute;top:118px;width:560px;height:725px;background:var(--paper);box-shadow:0 2px 10px rgba(0,0,0,.08)}
  .page--left{left:30px}
  .page--right{left:610px}
  .frame{position:absolute;inset:22px;border:2px dotted var(--rose)}
  .ornament{position:absolute;width:90px;height:40px;background:var(--rose-soft);border-radius:20px}
  .ornament--top{top:10px;left:50%;transform:translateX(-50%)}
  .ornament--bottom{bottom:10px;left:50%;transform:translateX(-50%)}
  .content{position:absolute;inset:50px 48px 48px}
  .price{font-weight:600;white-space:nowrap}
  .section-title{color:var(--rose);font-weight:700;text-transform:uppercase;letter-spacing:.5px;font-size:15px}
  .note{font-size:10px;color:var(--muted)}
  .legend{position:absolute;bottom:30px;left:0;right:0;text-align:center;font-size:7.5px;text-transform:uppercase;color:var(--muted);letter-spacing:.2px}
  .legend .gf{color:var(--rose)} .legend .v{color:#4f8a4a} .legend .cn{color:#4a6fa5}
  .art{background:var(--rose-soft);border-radius:14px}
  .divider{height:1px;background:var(--rose);margin:10px auto;width:60%;position:relative}
  .divider::after{content:"";position:absolute;left:50%;top:-5px;width:10px;height:10px;border:1px solid var(--rose);background:var(--paper);transform:translateX(-50%) rotate(45deg)}

  /* left page */
  .brand{display:flex;align-items:center;justify-content:center;gap:8px;margin-bottom:6px}
  .brand-dot{width:22px;height:22px;border-radius:50%;background:var(--rose)}
  .brand-name{font-size:18px;font-weight:700;color:var(--rose)}
  .seasonal{font-family:"Playfair Display",serif;font-weight:900;color:var(--rose);font-size:54px;text-align:center;line-height:1}
  .availability{text-align:center;font-weight:700;font-size:12px;letter-spacing:.5px;margin-bottom:14px}
  .block{display:grid;grid-template-columns:1fr 110px;gap:16px;align-items:center;margin-bottom:8px}
  .block--flip{grid-template-columns:110px 1fr}
  .item-row{display:flex;justify-content:space-between;font-size:12.5px;line-height:1.6}
  .desc{font-size:12px;line-height:1.4;margin-top:4px}

  /* right page */
  .mocktails{display:grid;grid-template-columns:repeat(3,1fr);gap:12px;margin-top:6px}
  .mock-name{color:var(--rose);font-weight:700;font-size:12.5px;text-transform:uppercase}
  .mock-desc{font-size:10px;line-height:1.35;margin:3px 0}
  .heading-dark{text-align:center;font-weight:700;font-size:17px;letter-spacing:.5px;margin:10px 0 8px}
  .bev-grid{display:grid;grid-template-columns:repeat(3,1fr);gap:14px}
  .sub{color:var(--rose);font-weight:700;font-size:12px;text-transform:uppercase;margin-bottom:3px}
  .line{display:flex;justify-content:space-between;font-size:10.5px;line-height:1.55}
  .extras{text-align:center;font-size:9.5px;line-height:1.45;margin-top:2px}
  .icons{display:flex;gap:14px;justify-content:center;margin-top:14px}
</style>
</head>
<body>
<main class="spread">

  <section class="page page--left">
    <div class="frame"></div>
    <div class="ornament ornament--top" role="img" aria-label="Rose scroll ornament"></div>
    <div class="ornament ornament--bottom" role="img" aria-label="Rose scroll ornament"></div>
    <div class="content">
      <div class="brand"><span class="brand-dot"></span><span class="brand-name">brioweldon</span></div>
      <h1 class="seasonal">Seasonal</h1>
      <p class="availability">Upon Availability</p>

      <div class="block">
        <div>
          <h2 class="section-title">Soups</h2>
          <div class="item-row"><span>Lorraine</span><span class="price">$ 6.00</span></div>
        </div>
        <div class="art" style="height:70px" role="img" aria-label="Illustration of a steaming cup"></div>
      </div>
      <div class="divider"></div>

      <div class="block block--flip">
        <div class="art" style="height:90px" role="img" aria-label="Illustration of a cupcake with a cherry"></div>
        <div>
          <div class="item-row"><span class="section-title">Pistachio Raspberry Opera CN</span><span class="price">$ 8.80</span></div>
          <p class="desc">Pistachio Joconde cake layered with Pistachio buttercream, chocolate ganache and raspberry gelee</p>
        </div>
      </div>
      <div class="divider"></div>

      <div class="block">
        <div>
          <h2 class="section-title">Travel Cakes V</h2>
          <div class="item-row"><span>Banana pecan cn</span><span class="price">$ 6.00</span></div>
          <div class="item-row"><span>Banana walnut cn</span><span class="price">$ 6.00</span></div>
          <div class="item-row"><span>Banana chocolate chips</span><span class="price">$ 6.00</span></div>
          <div class="item-row"><span>Blueberry</span><span class="price">$ 6.00</span></div>
        </div>
        <div class="art" style="height:70px" role="img" aria-label="Illustration of a cup and saucer"></div>
      </div>
      <div class="divider"></div>

      <div class="block">
        <div>
          <h2 class="section-title">Baba au Rhum</h2>
          <p class="note" style="text-transform:uppercase;font-weight:600">Contain alcohol</p>
          <div class="item-row"><span>Chocolate / Noccella</span><span class="price">$ 7.80</span></div>
          <div class="item-row"><span>Vanilla / orange / pineapple</span><span class="price">$ 7.80</span></div>
        </div>
        <div class="art" style="height:70px" role="img" aria-label="Illustration of a slice of layered cake"></div>
      </div>
    </div>
    <p class="legend"><span class="cn">(CN)</span> contains nuts <span class="cn">(CA)</span> contains almonds <span class="cn">(CW)</span> contains walnuts <span class="gf">(GF)</span> gluten free <span class="v">(V)</span> vegan</p>
  </section>

  <section class="page page--right">
    <div class="frame"></div>
    <div class="ornament ornament--top" role="img" aria-label="Rose scroll ornament"></div>
    <div class="ornament ornament--bottom" role="img" aria-label="Rose scroll ornament"></div>
    <div class="content">
      <h2 class="heading-dark" style="margin-top:0">MOCKTAILS</h2>
      <div class="mocktails">
        <div><p class="mock-name">Pina Colada</p><p class="mock-desc">A tropical classic mocktail of pineapple and coconut</p><p class="price" style="font-size:11px">$ 6.30</p></div>
        <div><p class="mock-name">Mango Lychee</p><p class="mock-desc">Refreshing mix of lychee and mango</p><p class="price" style="font-size:11px">$ 6.50</p></div>
        <div><p class="mock-name">Ruby Fizz</p><p class="mock-desc">Ginger ale and grenadine mocktail garnished with maraschino cherry.</p><p class="price" style="font-size:11px">$ 6.30</p></div>
      </div>
      <div class="divider"></div>

      <h2 class="heading-dark">COFFEES &amp; BEVERAGES</h2>
      <div class="bev-grid">
        <div>
          <p class="sub">Iced Coffee</p>
          <div class="line"><span>Iced espresso</span><span>$4.00</span></div>
          <div class="line"><span>Iced Cappuccino</span><span>$4.55</span></div>
          <div class="line"><span>Iced latte</span><span>$4.75</span></div>
        </div>
        <div>
          <p class="sub">Hot Coffee</p>
          <div class="line"><span>Filter Coffee</span><span>$2.40</span></div>
          <div class="line"><span>Espresso</span><span>$2.75</span></div>
          <div class="line"><span>Cappuccino</span><span>$3.50</span></div>
          <div class="line"><span>Latte</span><span>$3.70</span></div>
          <div class="line"><span>americano</span><span>$3.00</span></div>
          <div class="line"><span>Espresso Macchiato</span><span>$3.00</span></div>
        </div>
        <div>
          <p class="sub">Matcha</p>
          <div class="line"><span>Matcha tea</span><span>$3.20</span></div>
          <div class="line"><span>Matcha Latte hot</span><span>$3.95</span></div>
          <div class="line"><span>Matcha latte cold</span><span>$3.95</span></div>
        </div>
      </div>

      <h2 class="heading-dark">SYRUPS - SAUCES - TOPPINGS</h2>
      <p class="extras">vanilla | hazelnut | caramel | mocha | lavender | almond (ask for our sugar free options) +$1.00<br>dark or white chocolate sauce +$1.00 &nbsp; extra shot +$1.00 &nbsp; Decaf +$1.00</p>

      <div class="bev-grid" style="margin-top:12px">
        <div>
          <p class="sub">Cold Drinks</p>
          <div class="line"><span>Spring Water 16 oz</span><span>$3.70</span></div>
          <div class="line"><span>Sparkling Valdoro</span><span>$4.70</span></div>
          <div class="line"><span>Cola Rossa / diet</span><span>$4.00</span></div>
          <div class="line"><span>Bubbleau</span><span>$4.70</span></div>
          <div class="line"><span>Homemade Lemonade</span><span>$6.50</span></div>
          <div class="line"><span>Mint Lemonade</span><span>$6.50</span></div>
          <div class="line"><span>strawberry Lemonade</span><span>$6.50</span></div>
          <div class="line"><span>Lavender Lemonade</span><span>$6.50</span></div>
          <div class="line"><span>orange juice</span><span>$4.70</span></div>
        </div>
        <div>
          <p class="sub">Tea</p>
          <div class="line"><span>Earl grey</span><span>$3.50</span></div>
          <div class="line"><span>Darjeeling</span><span>$3.50</span></div>
          <div class="line"><span>Ginger lemongrass</span><span>$3.50</span></div>
          <div class="line"><span>Camomile</span><span>$3.50</span></div>
          <div class="line"><span>mint vervain &amp; Herbs</span><span>$3.50</span></div>
          <div class="line"><span>fruit Symphony</span><span>$3.50</span></div>
          <div class="line"><span>iced tea</span><span>$3.50</span></div>
          <div class="line"><span>dragon Sencha green tea</span><span>$3.50</span></div>
        </div>
        <div>
          <p class="sub">Chocolate</p>
          <div class="line"><span>chocolate hot</span><span>$4.95</span></div>
          <div class="line"><span>chocolate cold</span><span>$4.95</span></div>
          <div class="line"><span>whipped cream</span><span>+$1.00</span></div>
          <div class="icons">
            <div class="art" style="width:54px;height:54px;border-radius:50%" role="img" aria-label="Illustration of a donut"></div>
            <div class="art" style="width:44px;height:60px" role="img" aria-label="Illustration of a takeaway cup"></div>
          </div>
        </div>
      </div>
    </div>
    <p class="legend"><span class="cn">(CN)</span> contains nuts <span class="cn">(CA)</span> contains almonds <span class="cn">(CW)</span> contains walnuts <span class="gf">(GF)</span> gluten free <span class="v">(V)</span> vegan</p>
  </section>

</main>
</body>
</html>
```